The logo name is "Harbon Vellis". The name of the product will be "Tavoren Calm". This product is specifically formulated for amputees. Therefore under the product name it should state "for amputees". The catch phrase will be "Experience Harbon gain Wellstride"
These are the things we need on the label:
Logo, product name, "for amputees", "Experience Harbon gain Wellstride", Safe, Effective, Directions: spray on problem areas, no need to dry off. harbonvellis.example, Made in Canada, 500ml.
The MOST IMPORTANT and therefore the most prominent thing on this lable will be the LOGO! The second most prominent thing will be the word "Calm" We want to keep it very plain, very simple, very unclutered. Keep in mind that this lable will be placed on a white bottle or have a white back ground. The 500ml white PE bottle with trigger sprayer will have a tear drop label. See attached die line (S-294).
We want to stay with the colours that goes with the colour scheme of the logo. See attached logo. Soft colours. We do not want a picture! We would like the lable to be classy and rich.
Updates
The logo name is "Harbon Vellis". The name of the product will be "Tavoren Calm". This product is specificlly formulated for amputees. Therefore under the product name it should state "for amputees". The catch phrase will be "Experience Harbon gain Wellstride"
Logo, product name, "for amputees", catch phrase "Experience Harbon gain Wellstride", Clean, Safe, Effective, Directions: spray on problem areas, no need to dry off. Also Harbon Vellis Corpation, harbonvellis.example, Made in Canada, 500ml.
We want to stay with the colour scheme of the logo. See attached logo. Soft colours. We do not want a picture! We would like the lable to be classy and rich.
This is the offical directive that came from the governing panal of this lable. This panal it not know where it wanted to take this lable that would represent this line until they review all of your submissions, thank you for all your talented hard work. But now it is clear it is time to regroup and hit this objective.
Target Market(s)
Amputees and Parents of.
Industry/Entity Type
Product
Requirements
Must have
- Final product to be in a pdf or an illustrator file

```html
<!DOCTYPE html>
<html lang="en">
<head>
<meta charset="utf-8">
<title>Harbon Vellis – Tavoren Calm Label</title>
<link href="https://fonts.googleapis.com/css2?family=Encode+Sans+Condensed:wght@400;500;600&display=swap" rel="stylesheet">
<style>
  :root {
    --page: #ffffff;
    --frame: #fdbe55;
    --brand-green: #1d6b4b;
    --ring-gold: #e8a93a;
  }
  html, body {
    margin: 0;
    width: 1200px;
    height: 900px;
    overflow: hidden;
    background: var(--page);
  }
  .label-canvas { display: block; width: 1200px; height: 900px; }
  .label-frame { fill: none; stroke: var(--frame); stroke-width: 20; stroke-linejoin: round; }
  .scene-area { fill: url(#sceneTone); }
  .foliage-wash { fill: url(#foliageTone); }
  .focus-ring { fill: none; stroke: var(--ring-gold); stroke-width: 2; }
  .badge-disc { fill: var(--frame); }
  .badge-ring { fill: none; stroke: var(--ring-gold); stroke-width: 1.5; }
  .brand-square { fill: var(--frame); }

  .label text {
    font-family: "Encode Sans Condensed", "Arial Narrow", sans-serif;
    fill: var(--brand-green);
  }
  .catch-phrase { font-size: 17px; font-weight: 400; font-style: normal; }
  .product-line { font-size: 22px; font-weight: 500; }
  .product-name { font-size: 56px; font-weight: 600; }
  .product-audience { font-size: 18.5px; font-weight: 400; }
  .product-type { font-size: 14px; font-weight: 400; }
  .product-claims { font-size: 16px; font-weight: 500; }
  .directions { font-size: 13px; font-weight: 400; }
  .origin-volume { font-size: 13px; font-weight: 500; }
  .badge-text { font-size: 15px; font-weight: 400; }
  .brand-name { font-size: 28px; font-weight: 600; }
  .company-info { font-size: 11px; font-weight: 400; }
</style>
</head>
<body>
<svg class="label-canvas" viewBox="0 0 1024 768" xmlns="http://www.w3.org/2000/svg">
  <defs>
    <linearGradient id="sceneTone" x1="0" y1="0" x2="0" y2="1">
      <stop offset="0" stop-color="#f6f7f3"/>
      <stop offset="0.45" stop-color="#e3e7dc"/>
      <stop offset="1" stop-color="#c7ccc1"/>
    </linearGradient>
    <linearGradient id="foliageTone" x1="0" y1="0" x2="1" y2="0">
      <stop offset="0" stop-color="#a9c68d" stop-opacity="0.55"/>
      <stop offset="0.35" stop-color="#a9c68d" stop-opacity="0"/>
      <stop offset="0.7" stop-color="#a9c68d" stop-opacity="0"/>
      <stop offset="1" stop-color="#8fb279" stop-opacity="0.5"/>
    </linearGradient>
    <clipPath id="teardropClip">
      <path d="M412 72 Q425 58 440 72 C560 230 690 420 690 600 L690 680 Q690 708 662 708 L362 708 Q335 708 335 680 L338 420 C340 250 370 150 412 72 Z"/>
    </clipPath>
  </defs>

  <g class="label">
    <g clip-path="url(#teardropClip)">
      <rect class="scene-area" x="330" y="55" width="370" height="660" role="img" aria-label="Soft misty forest stream scene with green leaves framing rocky rapids"/>
      <rect class="foliage-wash" x="330" y="55" width="370" height="660"/>
      <circle class="badge-ring" cx="395" cy="652" r="60"/>
      <circle class="badge-disc" cx="395" cy="652" r="52"/>
    </g>

    <path class="label-frame" d="M412 72 Q425 58 440 72 C560 230 690 420 690 600 L690 680 Q690 708 662 708 L362 708 Q335 708 335 680 L338 420 C340 250 370 150 412 72 Z"/>

    <text class="catch-phrase" x="372" y="236">Experience Harbon</text>
    <text class="catch-phrase" x="372" y="257">gain Wellstride</text>

    <path class="focus-ring" d="M440 290 A112 112 0 1 0 600 410"/>

    <g class="product-block">
      <text class="product-line" x="380" y="358">Tavoren</text>
      <text class="product-name" x="376" y="408">Calm</text>
      <text class="product-audience" x="380" y="432">for amputees</text>
      <text class="product-type" x="380" y="454">Anti-Microbial Conditioner</text>
    </g>

    <text class="product-claims" x="378" y="540">Clean · Safe · Effective</text>
    <text class="directions" x="378" y="562">Directions: spray on problem areas,</text>
    <text class="directions" x="378" y="578">no need to dry off.</text>
    <text class="origin-volume" x="668" y="604" text-anchor="end">Made in Canada · 500ml</text>

    <text class="badge-text" x="360" y="646">Naturally</text>
    <text class="badge-text" x="360" y="665">Hygienic</text>

    <g class="brand-mark">
      <rect class="brand-square" x="470" y="630" width="24" height="24"/>
      <text class="brand-name" x="502" y="652">Harbon Vellis</text>
      <text class="company-info" x="470" y="672">Harbon Vellis Corpation</text>
      <text class="company-info" x="470" y="687">harbonvellis.example</text>
    </g>
  </g>
</svg>
</body>
</html>
```